Eye catching business card using our brand new logo
Dorvik Fabrication, Inc.
Modern
Wendell R. Fostrey
President
58 Quarry Hollow Road
Brindle, NH 03419
WFostrey@norvax.net
We would like to see many different styles of our brand new logo used in our business cards. Some would fill the card with the logo and some using it in the lower left corner of the card

```html
<!DOCTYPE html>
<html lang="en">
<head>
<meta charset="utf-8">
<title>Dorvik Fabrication, Inc. — Business Card</title>
<link rel="stylesheet" href="https://fonts.googleapis.com/css2?family=Open+Sans:wght@400;600;700&display=swap">
<style>
  :root {
    --backdrop: #ececef;
    --card: #ffffff;
    --brand-blue: #2f3f9e;
    --swoosh-blue: #3d4fc4;
    --swoosh-light: #8e9be6;
    --arc-gray: #8a8d94;
    --text-gray: #5b5e66;
    --divider: #c9cbd1;
    --faint: #e4e5e9;
  }
  * { box-sizing: border-box; margin: 0; padding: 0; }
  html, body {
    width: 1200px; height: 980px; overflow: hidden;
    background: var(--backdrop);
    font-family: "Open Sans", Arial, sans-serif;
  }
  .canvas { position: relative; width: 1200px; height: 980px; }

  .card {
    position: absolute;
    width: 700px; height: 400px;
    background: var(--card);
    border-radius: 28px;
    overflow: hidden;
    box-shadow: 0 6px 18px rgba(0,0,0,0.12);
  }
  .card--back { left: 440px; top: 80px; }
  .card--front { left: 60px; top: 500px; }

  .card__art { position: absolute; inset: 0; }

  /* Back */
  .back__url {
    position: absolute;
    left: 40px; top: 200px;
    transform: translate(-50%, -50%) rotate(90deg) translate(0, 0);
    transform-origin: center;
    font-size: 16px; letter-spacing: 7px;
    color: var(--text-gray);
    white-space: nowrap;
  }
  .back__mark {
    position: absolute; right: 60px; top: 150px;
    display: flex; align-items: center; gap: 14px;
  }
  .back__mark-dot {
    width: 150px; height: 150px; border-radius: 50%;
    background: var(--faint);
  }
  .back__mark-name {
    font-size: 22px; font-weight: 700; color: var(--faint);
    width: 150px; line-height: 1.2;
  }

  /* Front */
  .brand {
    position: absolute; left: 60px; top: 150px;
    display: flex; align-items: center; gap: 12px;
  }
  .brand__dot {
    width: 54px; height: 54px; border-radius: 50%;
    background: var(--arc-gray);
  }
  .brand__name {
    font-size: 19px; font-weight: 700; color: var(--brand-blue);
    line-height: 1.15; width: 170px;
  }
  .divider {
    position: absolute; left: 330px; top: 140px;
    width: 1px; height: 190px; background: var(--divider);
  }
  .contact { position: absolute; left: 350px; top: 140px; }
  .contact__name { font-size: 19px; font-weight: 700; color: var(--brand-blue); }
  .contact__title { font-size: 15px; color: var(--text-gray); margin-bottom: 12px; }
  .contact__list { list-style: none; }
  .contact__item {
    display: flex; align-items: flex-start; gap: 9px;
    font-size: 14px; line-height: 1.35; color: var(--text-gray);
    margin-bottom: 5px;
  }
  .contact__icon {
    flex: 0 0 18px; width: 18px; height: 18px; margin-top: 1px;
  }
</style>
</head>
<body>
<main class="canvas">

  <section class="card card--back" aria-label="Card back">
    <div class="back__url">www.dorvikfab.com</div>
    <div class="back__mark">
      <span class="back__mark-dot"></span>
      <span class="back__mark-name">Dorvik Fabrication, Inc.</span>
    </div>
  </section>

  <section class="card card--front" aria-label="Card front">
    <svg class="card__art" viewBox="0 0 700 400" aria-hidden="true">
      <defs>
        <linearGradient id="swoosh" x1="0" y1="0" x2="1" y2="0">
          <stop offset="0" stop-color="var(--swoosh-blue)"/>
          <stop offset="0.7" stop-color="var(--swoosh-light)"/>
          <stop offset="1" stop-color="#ffffff" stop-opacity="0"/>
        </linearGradient>
      </defs>
      <path d="M0 240 C 120 300, 260 330, 460 360 C 560 375, 650 385, 700 392 L700 400 L0 400 Z" fill="url(#swoosh)"/>
      <path d="M0 300 C 140 345, 300 372, 520 390 L 700 400 L0 400 Z" fill="var(--swoosh-blue)"/>
      <path d="M0 218 C 140 290, 300 320, 520 345" fill="none" stroke="var(--arc-gray)" stroke-width="5" stroke-linecap="round"/>
    </svg>

    <div class="brand">
      <span class="brand__dot"></span>
      <span class="brand__name">Dorvik Fabrication, Inc.</span>
    </div>

    <div class="divider"></div>

    <div class="contact">
      <p class="contact__name">Wendell R. Fostrey</p>
      <p class="contact__title">President</p>
      <ul class="contact__list">
        <li class="contact__item">
          <svg class="contact__icon" viewBox="0 0 18 18"><circle cx="9" cy="9" r="9" fill="var(--brand-blue)"/><path d="M9 4a3 3 0 0 0-3 3c0 2.4 3 6 3 6s3-3.6 3-6a3 3 0 0 0-3-3zm0 4.2a1.2 1.2 0 1 1 0-2.4 1.2 1.2 0 0 1 0 2.4z" fill="#fff"/></svg>
          <span>58 Quarry Hollow Road<br>Brindle, NH 03419</span>
        </li>
        <li class="contact__item">
          <svg class="contact__icon" viewBox="0 0 18 18"><circle cx="9" cy="9" r="9" fill="var(--brand-blue)"/><path d="M6.2 4.5l1.6 1.8-.8 1.3c.6 1.3 1.6 2.3 2.9 2.9l1.3-.8 1.8 1.6-.9 1.6c-3.4-.3-6.5-3.4-6.8-6.8z" fill="#fff"/></svg>
          <span>(603) 555-0142</span>
        </li>
        <li class="contact__item">
          <svg class="contact__icon" viewBox="0 0 18 18"><circle cx="9" cy="9" r="9" fill="var(--brand-blue)"/><rect x="5" y="4" width="8" height="10" rx="1" fill="#fff"/><rect x="6.5" y="5.5" width="5" height="3" fill="var(--brand-blue)"/></svg>
          <span>(603) 555-0187</span>
        </li>
        <li class="contact__item">
          <svg class="contact__icon" viewBox="0 0 18 18"><circle cx="9" cy="9" r="9" fill="var(--brand-blue)"/><rect x="4.5" y="6" width="9" height="6.5" fill="#fff"/><path d="M4.5 6l4.5 3.6L13.5 6" fill="none" stroke="var(--brand-blue)" stroke-width="1"/></svg>
          <span>WFostrey@norvax.net</span>
        </li>
      </ul>
    </div>
  </section>

</main>
</body>
</html>
```